Roll label Flyer design

I need a flyer for a roll label printer
Pictures for the project are located here:
https://plimtonstickers.sharefile.com/d-k4wq7812m3a0z551

Text I want is located here:
https://plimtonstickers.com/roll-labels.php

Target Market(s)

Manufactures, wholesalers

Industry/Entity Type

Printing

Requirements
Must have
• Lots of pictures. Our phone number 800-472-8164. Website www.plimtonstickers.com

```html
<!DOCTYPE html>
<html lang="en">
<head>
<meta charset="utf-8">
<title>Roll/Product Labels – Plimton Stickers</title>
<link rel="stylesheet" href="https://fonts.googleapis.com/css2?family=Russo+One&family=Saira:wght@400;600&display=swap">
<style>
  :root {
    --red: #b5090d;
    --red-dark: #7a0508;
    --grey-tag: #4a4a4c;
    --ink: #1f1f21;
    --white: #ffffff;
    --photo-top: #8e8b88;
    --photo-mid: #5a5856;
    --photo-bottom: #262626;
  }
  * { box-sizing: border-box; margin: 0; padding: 0; }
  html, body { width: 933px; height: 1200px; overflow: hidden; background: var(--white); }
  .flyer { position: relative; width: 933px; height: 1200px; font-family: "Saira", sans-serif; color: var(--white); }

  .hero {
    position: absolute; left: 0; top: 0; width: 933px; height: 716px;
    background: linear-gradient(180deg, var(--photo-top) 0%, #7a7774 35%, var(--photo-mid) 62%, var(--photo-bottom) 100%);
  }

  .intro {
    position: absolute; left: 228px; top: 0; width: 476px; height: 214px;
    background: var(--red); padding: 26px 46px 0 48px;
  }
  .intro-fold { position: absolute; left: 228px; top: 184px; }
  .intro h1 {
    font-family: "Russo One", sans-serif; font-weight: 400; font-size: 33px;
    text-align: center; letter-spacing: 0.5px; margin-bottom: 10px;
  }
  .intro p { font-size: 17.2px; line-height: 22.5px; text-align: justify; letter-spacing: 0.3px; }

  .feature {
    position: absolute; height: 40px; display: flex; align-items: center; justify-content: center;
    font-size: 23px; letter-spacing: 0.4px;
  }
  .feature.red { background: var(--red); }
  .feature.grey { background: var(--grey-tag); }

  .markets-title {
    position: absolute; left: 0; top: 503px; width: 933px; text-align: center;
    font-family: "Russo One", sans-serif; font-size: 22px; letter-spacing: 0.5px;
  }
  .market { position: absolute; top: 554px; width: 140px; text-align: center; }
  .market-icon {
    width: 92px; height: 92px; margin: 0 auto; border-radius: 50%;
    background: var(--red); border: 3px solid var(--white);
    display: flex; align-items: center; justify-content: center;
  }
  .market-name { margin-top: 20px; font-size: 15px; line-height: 19px; letter-spacing: 0.3px; }

  .gallery .shot { position: absolute; }
  .shot.a { background: linear-gradient(180deg, #6e6a66, #9c9a98 50%, #4d4b49); }
  .shot.b { background: linear-gradient(135deg, #5a4a3e, #a8262a 55%, #3b3632); }
  .shot.c { background: linear-gradient(135deg, #8e8f94, #3e5e90 55%, #5c5d61); }
  .shot.d { background: linear-gradient(135deg, #8f8a80, #1f2430 55%, #a8a8a8); }
  .shot.e { background: linear-gradient(135deg, #3a3530, #c9b48f 45%, #d8d8d8); }
  .shot.f { background: linear-gradient(135deg, #3a3734, #e7a640 50%, #e8e6e2); }
  .shot.g { background: linear-gradient(135deg, #2d2d2d, #6e6e6e 55%, #cfcfcf); }

  .footer-brand {
    position: absolute; left: 0; top: 1058px; width: 466px; height: 142px;
    background: var(--ink); display: flex; align-items: center; padding-left: 70px; gap: 18px;
  }
  .brand-mark { width: 58px; height: 58px; border-radius: 50%; background: var(--red); }
  .brand-name { font-family: "Saira", sans-serif; font-weight: 600; font-size: 26px; letter-spacing: 6px; }

  .footer-contact {
    position: absolute; left: 466px; top: 1058px; width: 467px; height: 142px;
    background: var(--red); padding: 26px 0 0 14px; font-family: "Russo One", sans-serif;
  }
  .contact-line { display: flex; align-items: center; gap: 12px; }
  .contact-line.phone { font-size: 36px; letter-spacing: 1px; }
  .contact-line.web { font-size: 21px; margin-top: 10px; letter-spacing: 0.4px; }
</style>
</head>
<body>
<main class="flyer">
  <div class="hero" role="img" aria-label="Label press operator working beside a roll label printing machine on the factory floor"></div>

  <section class="intro">
    <h1>Roll/Product Labels</h1>
    <p>Long or short run. Digital or flexographic. Standard shapes or unique, custom diecuts. Simple spot colors or full color with every embellishment. Let us help you create the perfect label for your application.</p>
  </section>
  <svg class="intro-fold" width="32" height="30" viewBox="0 0 32 30"><polygon points="0,0 32,0 32,30" fill="var(--red-dark)"/></svg>

  <div class="feature red" style="left:148px;top:304px;width:164px;">Embossing</div>
  <div class="feature grey" style="left:353px;top:304px;width:193px;">Foil-Stamping</div>
  <div class="feature red" style="left:586px;top:304px;width:222px;">Spot Varnishes</div>
  <div class="feature grey" style="left:60px;top:366px;width:386px;">Instant Redeemable Coupons</div>
  <div class="feature red" style="left:486px;top:366px;width:386px;">Expanded Content/Booklet Labels</div>

  <h2 class="markets-title">Specialty Markets We Service Include:</h2>

  <div class="market" style="left:56px;">
    <div class="market-icon">
      <svg width="52" height="52" viewBox="0 0 52 52" fill="#fff"><path d="M6 4h18l-3 30h-4l-1 6h-4l-1-6H8z"/><rect x="24" y="20" width="8" height="6"/><rect x="20" y="26" width="22" height="20" rx="4"/><rect x="29" y="31" width="4" height="10" fill="var(--red)"/><rect x="26" y="34" width="10" height="4" fill="var(--red)"/></svg>
    </div>
    <div class="market-name">Health &amp; Beauty</div>
  </div>
  <div class="market" style="left:193px;">
    <div class="market-icon">
      <svg width="52" height="52" viewBox="0 0 52 52" fill="none" stroke="#fff" stroke-width="5" stroke-linecap="round"><path d="M10 44L40 14"/><ellipse cx="41" cy="11" rx="6" ry="8" transform="rotate(45 41 11)" fill="#fff" stroke="none"/><path d="M42 44L14 16"/><path d="M8 8l10 10M14 4l8 8M4 14l8 8" stroke-width="3"/></svg>
    </div>
    <div class="market-name">Food &amp; Beverage</div>
  </div>
  <div class="market" style="left:329px;">
    <div class="market-icon">
      <svg width="52" height="56" viewBox="0 0 52 56" fill="#fff"><path d="M4 18h16c0 10-3 14-8 14S4 28 4 18z"/><rect x="11" y="31" width="3" height="15"/><rect x="6" y="45" width="13" height="3"/><rect x="33" y="2" width="6" height="12"/><path d="M31 14h10l4 8v30H27V22z"/><rect x="29" y="28" width="14" height="12" fill="var(--red)"/></svg>
    </div>
    <div class="market-name">Wine &amp; Spirits</div>
  </div>
  <div class="market" style="left:466px;">
    <div class="market-icon">
      <svg width="56" height="52" viewBox="0 0 56 52" fill="#fff"><path d="M14 22a14 14 0 0 1 28 0z"/><rect x="11" y="22" width="34" height="4" rx="2"/><path d="M2 22l6 18 14 8h6V38l-10-6-6-12z"/><path d="M54 22l-6 18-14 8h-6V38l10-6 6-12z"/></svg>
    </div>
    <div class="market-name">Industrial Safety<br>&amp; Warning</div>
  </div>
  <div class="market" style="left:602px;">
    <div class="market-icon">
      <svg width="52" height="52" viewBox="0 0 52 52" fill="none" stroke="#fff" stroke-width="3.5" stroke-linejoin="round"><rect x="6" y="10" width="36" height="26" rx="2"/><path d="M24 36v8M16 46h16"/><path d="M14 28l12-10 6 16z" fill="#fff"/><path d="M40 8l6-4M42 14h7M40 20l6 3"/></svg>
    </div>
    <div class="market-name">Promotional</div>
  </div>
  <div class="market" style="left:739px;">
    <div class="market-icon">
      <svg width="52" height="52" viewBox="0 0 52 52" fill="none" stroke="#fff" stroke-width="3.5" stroke-linecap="round"><path d="M30 46H8V4h30v20"/><path d="M14 13h18M14 20h18M14 27h12"/><circle cx="38" cy="38" r="10"/><path d="M33 38l4 4 6-7"/></svg>
    </div>
    <div class="market-name">Compliance</div>
  </div>

  <section class="gallery">
    <div class="shot a" style="left:6px;top:722px;width:186px;height:328px;" role="img" aria-label="Rolls of printed warning labels running through the press"></div>
    <div class="shot b" style="left:198px;top:722px;width:242px;height:160px;" role="img" aria-label="Red danger warning labels on a roll"></div>
    <div class="shot c" style="left:446px;top:722px;width:223px;height:160px;" role="img" aria-label="Printing station of a flexographic label press"></div>
    <div class="shot d" style="left:676px;top:722px;width:251px;height:160px;" role="img" aria-label="Finished roll of dark product labels"></div>
    <div class="shot e" style="left:198px;top:888px;width:259px;height:162px;" role="img" aria-label="Rolls of printed product labels with metallic accents"></div>
    <div class="shot f" style="left:463px;top:888px;width:206px;height:162px;" role="img" aria-label="Orange striped labels feeding over a roller"></div>
    <div class="shot g" style="left:676px;top:888px;width:251px;height:162px;" role="img" aria-label="Die-cut labels being stripped on the press"></div>
  </section>

  <footer>
    <div class="footer-brand">
      <span class="brand-mark"></span>
      <span class="brand-name">PLIMTON STICKERS</span>
    </div>
    <div class="footer-contact">
      <div class="contact-line phone">
        <svg width="30" height="32" viewBox="0 0 24 24" fill="#fff"><path d="M6.6 10.8a15 15 0 0 0 6.6 6.6l2.2-2.2a1 1 0 0 1 1-.25 11.4 11.4 0 0 0 3.6.57 1 1 0 0 1 1 1V20a1 1 0 0 1-1 1A17 17 0 0 1 3 4a1 1 0 0 1 1-1h3.5a1 1 0 0 1 1 1c0 1.25.2 2.45.57 3.57a1 1 0 0 1-.25 1z"/></svg>
        <span>800-472-8164</span>
      </div>
      <div class="contact-line web">
        <svg width="30" height="30" viewBox="0 0 30 30" fill="none" stroke="#fff" stroke-width="2.5" stroke-linecap="round"><path d="M13 13l6 15 2-6 6-2z" fill="#fff"/><path d="M9 3v4M3 9h4M4.5 4.5l3 3M15 4.5l-3 3M4.5 15l3-3"/></svg>
        <span>Website www.plimtonstickers.com</span>
      </div>
    </div>
  </footer>
</main>
</body>
</html>
```